e-commerce website for selling flooring materials and related accessories

We are developing a new e-commerce site based in the US. We plan to sell all types of flooring - such as Hardwood, Laminate, Waterproof flooring and Porcelain tile, marble, Carpet, and related accessories.

OUR BACK END IS MAGENTO 2.

Target Market(s)

consumer, builder & contractors, hospitality industry, architect, designers, private sector

Industry/Entity Type

Flooring

Coding

Coded - Design and coding required

Number of Pages Required

5+ page

Font styles to use
Sans Serif

Requirements
Must have
• Logo placement, 3 Color combination, Banner placement, promotional pricing tags, check out page, blog placement, social media icons, 1800 number, product and related accessories placement. For reference purposes, please visit our competitor websites -
1.www.plankmeadowoutlet.example
2.tilebirchhome.example
3.www.grovewoodsurplus.example
4.www.shopkestrel.example
5.www.padmatcorp.example
Nice to have
• Our main customers are women and families and we want to make sure the design is attractive.
we like to have 2 or 3 bands at the top.
please provide design for the bottom page.
Should not have
• As our products are more natural colors, please do not bring extreme colors into the design

```html
<!DOCTYPE html>
<html lang="en">
<head>
<meta charset="utf-8">
<title>Floorvale – Flooring Store</title>
<link href="https://fonts.googleapis.com/css2?family=Kanit:wght@500;600&family=Lato:wght@400;700&display=swap" rel="stylesheet">
<style>
:root{
  --bark:#5a4330;
  --heading:#5b3f2a;
  --accent:#c18e5d;
  --accent-soft:#d3a87c;
  --text:#4a4a4a;
  --muted:#777;
  --line:#e6e1dc;
  --footer:#f6f4f1;
  --white:#fff;
}
*{box-sizing:border-box;margin:0;padding:0}
html,body{width:1200px;height:2690px;overflow:hidden;background:var(--white)}
body{font-family:"Lato",sans-serif;color:var(--text);position:relative}
.abs{position:absolute}
.display{font-family:"Kanit",sans-serif;font-weight:600;color:var(--heading)}
.topbar{left:0;top:0;width:1200px;height:34px;background:var(--bark);color:var(--white);font-size:13px}
.topbar span{position:absolute;top:9px;display:flex;align-items:center;gap:6px}
.topbar .sep{width:1px;height:16px;background:#fff;top:9px}
.header{left:0;top:34px;width:1200px;height:75px;border-bottom:1px solid #f0ece8}
.brand{display:flex;align-items:center;gap:8px;font-family:"Kanit",sans-serif;font-weight:600;font-size:27px;color:var(--bark)}
.brand i{display:block;width:26px;height:26px;border-radius:50%;background:var(--accent)}
.mainnav a{position:absolute;top:60px;font-size:13.5px;color:#444;text-decoration:none}
.search{left:888px;top:48px;width:235px;height:40px;border:2px solid #ddd;font-size:13px;color:#aaa;font-style:italic;padding:11px 14px}
.catnav{left:0;top:136px;width:1200px;display:flex;justify-content:center;gap:45px;font-size:13.5px;color:#444}
.hero{left:73px;top:179px;width:1049px;height:530px;background:linear-gradient(100deg,#cfcbc4 0%,#d8d2c9 38%,#bfb1a0 60%,#a89784 100%)}
.btn{display:flex;align-items:center;justify-content:center;background:var(--accent);color:var(--white);font-size:13.5px}
.dots{display:flex;gap:6px}
.dots b{width:10px;height:10px;border:1.5px solid #fff;display:block}
.section-title{left:0;width:1200px;text-align:center;font-size:30px}
.card-img{height:251px}
.card-title{text-align:center;font-family:"Kanit",sans-serif;font-weight:500;font-size:17px;line-height:22px;color:var(--heading)}
.card-size{text-align:center;font-size:13px;color:var(--muted)}
.card-price{text-align:center;font-family:"Kanit",sans-serif;font-weight:600;font-size:17px;color:var(--heading)}
.arrow{width:44px;height:44px;border-radius:50%;background:var(--white);box-shadow:0 4px 18px rgba(0,0,0,.12);display:flex;align-items:center;justify-content:center;z-index:2}
.tile{top:1827px;width:158px;height:157px;border:1px solid #eee;display:flex;flex-direction:column;align-items:center;padding-top:40px;background:var(--white)}
.tile .lbl{margin-top:20px;font-family:"Kanit",sans-serif;font-weight:500;font-size:13px;color:var(--heading);text-align:center;line-height:15px}
.tile.active{background:var(--accent);border:3px solid #fff;box-shadow:0 4px 14px rgba(0,0,0,.15)}
.tile.active .lbl{color:#fff}
.footer{left:0;top:2372px;width:1200px;height:281px;background:var(--footer)}
.fhead{font-family:"Kanit",sans-serif;font-weight:600;font-size:17px;color:var(--heading)}
.flist{font-size:13.5px;line-height:17.5px;color:#555}
.bottombar{left:0;top:2653px;width:1200px;height:37px;background:var(--bark);color:#fff;font-size:13.5px}
.pay{width:28px;height:18px;border-radius:3px;background:#e9e4de;display:inline-block}
.social{width:18px;height:18px;background:#d9cfc4;display:inline-block}
</style>
</head>
<body>

<div class="abs topbar">
  <span style="left:74px"><svg width="18" height="18" viewBox="0 0 24 24" fill="none" stroke="#fff" stroke-width="1.6"><path d="M5 3h4l2 5-3 2a12 12 0 0 0 6 6l2-3 5 2v4a2 2 0 0 1-2 2A17 17 0 0 1 3 5a2 2 0 0 1 2-2z"/></svg>(+00) 123-456-789</span>
  <span style="left:796px"><svg width="16" height="16" viewBox="0 0 24 24" fill="none" stroke="#fff" stroke-width="2"><circle cx="8" cy="8" r="5"/><path d="M12 12l9 9M17 17l3-3"/></svg>Login</span>
  <span class="sep" style="left:874px"></span>
  <span style="left:898px"><svg width="15" height="16" viewBox="0 0 24 24" fill="none" stroke="#fff" stroke-width="2"><circle cx="12" cy="8" r="5"/><path d="M3 22c1-5 5-7 9-7s8 2 9 7z"/></svg>Register</span>
  <span class="sep" style="left:985px"></span>
  <span style="left:1007px"><svg width="20" height="16" viewBox="0 0 26 22" fill="none" stroke="#fff" stroke-width="1.8"><path d="M1 2h4l3 13h14l3-9H7"/><circle cx="10" cy="19" r="1.6"/><circle cx="20" cy="19" r="1.6"/></svg>Items (0) $0.00</span>
</div>

<header class="abs header">
  <div class="abs brand" style="left:88px;top:20px"><i></i>Floorvale</div>
</header>
<nav class="mainnav">
  <a class="abs" style="left:612px">About us</a>
  <a class="abs" style="left:710px">Blogs</a>
  <a class="abs" style="left:788px">Contact us</a>
</nav>
<div class="abs search">Search
  <svg class="abs" style="right:12px;top:10px" width="18" height="18" viewBox="0 0 24 24" fill="none" stroke="#555" stroke-width="2"><circle cx="10" cy="10" r="7"/><path d="M15 15l7 7"/></svg>
</div>

<nav class="abs catnav">
  <span>Hardwood</span><span>Laminate</span><span>Waterproof flooring &amp; Porcelain tile</span><span>Marble</span><span>Carpet</span><span>Accessories</span>
</nav>

<section class="abs hero" role="img" aria-label="Bright empty room with pale oak hardwood floor and white kitchen"></section>
<div class="abs display" style="left:152px;top:380px;color:#fff;font-size:19px;font-weight:500">Making your home luxury with</div>
<div class="abs display" style="left:150px;top:405px;color:#fff;font-size:45px">HARDWOOD FLOOR</div>
<div class="abs btn" style="left:147px;top:483px;width:127px;height:39px">Shop Now</div>
<div class="abs dots" style="left:149px;top:636px"><b></b><b></b><b></b></div>

<h2 class="abs display section-title" style="top:775px">Feature Products</h2>

<div class="abs card-img" style="left:72px;top:853px;width:251px;background:linear-gradient(90deg,#9c6b45,#b98b62,#8e5f3c,#b5865c)" role="img" aria-label="Oak wood plank ceramic tile sample"></div>
<div class="abs card-title" style="left:72px;top:1131px;width:251px">Hollis creek ashford oak wood plank ceramic tile</div>
<div class="abs card-size" style="left:72px;top:1189px;width:251px">Size: 6 x 24</div>
<div class="abs card-price" style="left:72px;top:1218px;width:251px">$0.65 / Sq..ft</div>

<div class="abs" style="left:338px;top:853px;width:252px;height:428px;border:1.5px solid var(--accent-soft)"></div>
<div class="abs" style="left:350px;top:864px;width:228px;height:228px;background:linear-gradient(135deg,#7d6a5b,#8e7b6c,#76635a)" role="img" aria-label="Grey chevron marble mosaic sample"></div>
<div class="abs" style="left:529px;top:880px;width:38px;height:38px;border-radius:50%;background:#fff;display:flex;align-items:center;justify-content:center"><svg width="18" height="16" viewBox="0 0 24 22"><path d="M12 21L2 11a5.5 5.5 0 0 1 10-7 5.5 5.5 0 0 1 10 7z" fill="#b07b4b"/></svg></div>
<div class="abs" style="left:529px;top:927px;width:38px;height:38px;border-radius:50%;background:#fff;display:flex;align-items:center;justify-content:center"><svg width="18" height="18" viewBox="0 0 24 24" fill="none" stroke="#b07b4b" stroke-width="2"><path d="M20 12a8 8 0 0 1-14 5M4 12a8 8 0 0 1 14-5M18 3v4h-4M6 21v-4h4"/></svg></div>
<div class="abs card-title" style="left:338px;top:1131px;width:252px">Corrisa Dune gray chevron honed stone mosaic</div>
<div class="abs card-size" style="left:338px;top:1189px;width:252px">Size: 10 x 11</div>
<div class="abs btn" style="left:400px;top:1228px;width:128px;height:38px">Add To Cart</div>

<div class="abs card-img" style="left:604px;top:853px;width:252px;background:linear-gradient(135deg,#7a3c22,#a05a35,#6e3522,#9a6a4a)" role="img" aria-label="Red textured carpet sample"></div>
<div class="abs" style="left:604px;top:853px;width:70px;height:70px;overflow:hidden"><div style="position:absolute;left:-28px;top:18px;width:120px;height:18px;background:var(--accent-soft);transform:rotate(-45deg);color:#fff;font-size:11px;text-align:center;line-height:18px">New</div></div>
<div class="abs card-title" style="left:604px;top:1131px;width:252px">Red wood Alderly,Bright Perspective</div>
<div class="abs card-price" style="left:604px;top:1218px;width:252px">$1.20Sq..ft</div>

<div class="abs card-img" style="left:870px;top:853px;width:252px;background:linear-gradient(135deg,#b9aa9a,#8f7d6c,#c2b3a3,#7f6f60)" role="img" aria-label="Beige marble porcelain tile sample"></div>
<div class="abs card-title" style="left:870px;top:1131px;width:252px">Lindell, Moretti Porcelain Tile</div>
<div class="abs card-size" style="left:870px;top:1189px;width:252px">Size: 13X13</div>
<div class="abs card-price" style="left:870px;top:1218px;width:252px">$2.42Sq..ft</div>

<div class="abs arrow" style="left:51px;top:952px"><svg width="20" height="14" viewBox="0 0 20 14" fill="none" stroke="#b07b4b" stroke-width="2.4"><path d="M19 7H2M8 1L2 7l6 6"/></svg></div>
<div class="abs arrow" style="left:1102px;top:952px"><svg width="20" height="14" viewBox="0 0 20 14" fill="none" stroke="#b07b4b" stroke-width="2.4"><path d="M1 7h17M12 1l6 6-6 6"/></svg></div>

<section class="abs" style="left:73px;top:1378px;width:1049px;height:334px;background:linear-gradient(100deg,#8a8a70 0%,#c9c2b4 30%,#a77a55 60%,#8a4f2a 100%)" role="img" aria-label="Sunlit living room with warm hardwood floor and open patio door"></section>
<div class="abs display" style="left:661px;top:1458px;color:#fff;font-size:19px;font-weight:500">Get Discount</div>
<div class="abs display" style="left:661px;top:1488px;color:#fff;font-size:42px;line-height:53px">Get 20% Discont<br>on your first Order</div>
<div class="abs btn" style="left:661px;top:1608px;width:128px;height:38px">Shop Now</div>

<h2 class="abs display section-title" style="top:1758px">Shop by</h2>

<div class="abs tile active" style="left:127px">
  <svg width="40" height="40" viewBox="0 0 40 40" fill="none" stroke="#fff" stroke-width="1.5"><rect x="1" y="1" width="38" height="38"/><path d="M10 1v38M20 1v38M30 1v38M14 10c3 4 3 8 0 12M24 18c3 4 3 8 0 12"/></svg>
  <div class="lbl">Hardwood</div></div>
<div class="abs tile" style="left:285px">
  <svg width="40" height="40" viewBox="0 0 40 40" fill="none" stroke="#c18e5d" stroke-width="1.5"><rect x="1" y="1" width="38" height="38"/><path d="M1 14L14 1M1 27L27 1M1 39L39 1M13 39L39 13M26 39L39 26M1 14l25 25M14 1l25 25"/></svg>
  <div class="lbl">Laminate</div></div>
<div class="abs tile" style="left:443px">
  <svg width="40" height="40" viewBox="0 0 40 40" fill="none" stroke="#c18e5d" stroke-width="1.5"><rect x="1" y="1" width="38" height="38"/><path d="M1 12L12 1M1 24L24 1M1 36L36 1M8 39L39 8M20 39L39 20M32 39L39 32"/></svg>
  <div class="lbl">Waterproof flooring &amp;<br>Proceline tile</div></div>
<div class="abs tile" style="left:601px">
  <svg width="40" height="40" viewBox="0 0 40 40" fill="none" stroke="#c18e5d" stroke-width="1.5"><rect x="1" y="1" width="38" height="38"/><path d="M1 20c8-2 12 4 20 0s10-10 18-8M10 39c2-8 10-10 12-16"/></svg>
  <div class="lbl">Marbel</div></div>
<div class="abs tile" style="left:759px">
  <svg width="34" height="40" viewBox="0 0 34 40" fill="none" stroke="#c18e5d" stroke-width="1.5"><path d="M6 1h26v38H6M6 1a5 5 0 0 0 0 10v28M12 6v28M17 6v28M22 6v28M27 6v28"/></svg>
  <div class="lbl">Carpet</div></div>
<div class="abs tile" style="left:917px">
  <svg width="44" height="40" viewBox="0 0 44 40" fill="none" stroke="#c18e5d" stroke-width="2"><circle cx="6" cy="20" r="4"/><circle cx="22" cy="20" r="4"/><circle cx="38" cy="20" r="4"/></svg>
  <div class="lbl">Accessories</div></div>
<div class="abs arrow" style="left:99px;top:1882px"><svg width="20" height="14" viewBox="0 0 20 14" fill="none" stroke="#b07b4b" stroke-width="2.4"><path d="M19 7H2M8 1L2 7l6 6"/></svg></div>
<div class="abs arrow" style="left:1049px;top:1882px"><svg width="20" height="14" viewBox="0 0 20 14" fill="none" stroke="#b07b4b" stroke-width="2.4"><path d="M1 7h17M12 1l6 6-6 6"/></svg></div>

<h2 class="abs display section-title" style="top:2041px">Client`s Reviews</h2>
<div class="abs display" style="left:221px;top:2110px;font-size:24px;line-height:24px">“</div>
<p class="abs" style="left:226px;top:2124px;width:740px;text-align:center;font-size:13.5px;line-height:18px;color:#555">Lorem Ipsum is simply dummy text of the printing and typesetting industry. Lorem Ipsum has been the industry's standard dummy text ever since the 1500s, when an unknown printer took a galley of type and scrambled it to make a type specimen book.</p>
<div class="abs display" style="left:682px;top:2162px;font-size:24px;line-height:24px">”</div>
<div class="abs" style="left:0;top:2210px;width:1200px;text-align:center;font-family:'Kanit',sans-serif;font-weight:500;font-size:17px;color:var(--heading)">Marlow Pennick</div>
<div class="abs" style="left:0;top:2238px;width:1200px;text-align:center;color:#f0b400;font-size:13px;letter-spacing:1px">★★★★★</div>
<div class="abs" style="left:576px;top:2280px;display:flex;gap:8px"><b style="width:9px;height:9px;background:var(--accent)"></b><b style="width:9px;height:9px;border:1.5px solid var(--accent)"></b><b style="width:9px;height:9px;border:1.5px solid var(--accent)"></b></div>

<footer class="abs footer"></footer>
<div class="abs brand" style="left:153px;top:2413px"><i></i>Floorvale</div>
<p class="abs flist" style="left:153px;top:2483px;width:240px;line-height:18px">Lorem Ipsum is simply dummy text of the printing and typesetting industry. Lorem Ipsum has been the industry's standard dummy text.</p>
<div class="abs" style="left:152px;top:2600px;font-size:13.5px;color:var(--accent);display:flex;align-items:center;gap:10px">Read More <svg width="48" height="10" viewBox="0 0 48 10" fill="none" stroke="#c18e5d" stroke-width="1.5"><path d="M0 5h46M41 1l5 4-5 4"/></svg></div>

<div class="abs fhead" style="left:433px;top:2424px">Quick Links</div>
<div class="abs flist" style="left:432px;top:2483px">Home<br>About<br>Blogs<br>Reviews<br>Cotact us<br>Terms &amp; Conditon<br>Privacy policy</div>
<div class="abs fhead" style="left:587px;top:2424px">Products</div>
<div class="abs flist" style="left:587px;top:2483px;line-height:16.5px">Hardwood<br>Laminate<br>Porcelain tile<br>Marble<br>Carpet<br>Accessories</div>
<div class="abs fhead" style="left:723px;top:2424px">Accounts</div>
<div class="abs flist" style="left:722px;top:2483px;line-height:16.5px">Login<br>Register<br>My profile<br>My cart<br>Checkout</div>
<div class="abs fhead" style="left:841px;top:2424px">Newsletter</div>
<div class="abs" style="left:841px;top:2484px;width:209px;height:38px;background:#fbfaf8;font-size:12.5px;font-style:italic;color:#bbb;padding:11px 12px">Email Address</div>
<div class="abs btn" style="left:841px;top:2533px;width:128px;height:39px">Subscribe</div>
<div class="abs" style="left:841px;top:2598px;display:flex;gap:11px"><span class="social"></span><span class="social"></span><span class="social"></span><span class="social"></span><span class="social"></span></div>

<div class="abs bottombar">
  <span class="abs" style="left:153px;top:10px">Copyright © 2020 Floorvale. All rights reserved.</span>
  <span class="abs" style="left:839px;top:9px;display:flex;gap:8px"><i class="pay"></i><i class="pay"></i><i class="pay"></i><i class="pay"></i><i class="pay"></i><i class="pay"></i></span>
</div>

</body>
</html>
```